Funken-und-Fragen Flyer
Zielgruppe
Eltern, die ihre Kinder in ihrer Entwicklung fördern möchten.
Aufgabenstellung
Wir organisieren eine Messe mit dem Thema "Funken und Fragen". Bei der Messe geht es nicht um das Lernen über Bücher (alleine) oder das Schulische, sondern die Messe soll für Eltern sein, die ihre Kinder fördern möchten durch die Behebung von Lernblockaden, Förderung der Konzentration, Kreativität, spielerisches Lernen etc. Es geht um Kinder ab ca. 4 Jahren.
Als Aussteller werden verschiedene Themen angesprochen: Kinesiologie, Logopädie, Privatschulen mit speziellem Angenbot, Schachunterricht, spielerisches Lernangebot, Kindermalen etc. , alles was darauf zielt, Kreativität und Lernen bei Kindern zu fördern.
Wir brauchen daher einen Flyer, der die Eltern anspricht. Die Messe findet am Sonntag, 9.11.2012 statt. Beginn 11 Uhr, Ende 18.00 Uhr. Ort: Seeforumhalle - Lindensaal, Wendelgasse 7, 8047 Zürich.
Das Logo wird attached. Das Format ist frei wählbar.

```html
<!DOCTYPE html>
<html lang="de">
<head>
<meta charset="utf-8">
<title>Funken und Fragen – Messe Zürich</title>
<link rel="stylesheet" href="https://fonts.googleapis.com/css2?family=Anton&family=Open+Sans:wght@400&family=Roboto:wght@400;700&display=swap">
<style>
  :root {
    --stage: #b3c5c1;
    --paper: #ffffff;
    --orange: #ec9a00;
    --purple: #8c0079;
    --blue: #00a5e6;
    --teal: #2e8c93;
    --brand-teal: #2a9a94;
    --ink: #333333;
    --shadow: #1a1a1a;
    --rule: #ffffff;
  }
  * { margin: 0; padding: 0; box-sizing: border-box; }
  html, body { width: 1200px; height: 1200px; overflow: hidden; background: var(--stage); }
  .flyer {
    position: absolute; left: 191px; top: 25px;
    width: 818px; height: 1150px;
    background: var(--paper);
    overflow: hidden;
  }
  .headline-band {
    position: absolute; left: 0; top: 0; width: 553px; height: 148px;
    background: var(--orange);
    font-family: "Anton", Impact, sans-serif;
    color: #fff; font-size: 25px; line-height: 34px;
    text-shadow: 2px 2px 2px var(--shadow);
    padding-top: 28px;
  }
  .headline-band span { display: block; }
  .headline-band .l1 { padding-left: 38px; }
  .headline-band .l2 { padding-left: 80px; }
  .headline-band .l3 { padding-left: 118px; }
  .brand {
    position: absolute; left: 575px; top: 58px; width: 230px;
    text-align: center;
  }
  .brand-dot {
    width: 26px; height: 26px; border-radius: 50%;
    background: var(--brand-teal); margin: 0 auto 10px;
  }
  .brand-name {
    font-family: "Open Sans", Arial, sans-serif; font-size: 25px;
    color: var(--brand-teal); line-height: 1;
  }
  .brand-url {
    font-family: "Roboto", Arial, sans-serif; font-size: 10px; color: var(--ink);
    text-align: right; padding-right: 12px; margin-top: 4px;
  }
  .photo {
    position: absolute; left: 0; top: 148px; width: 818px; height: 470px;
    background: radial-gradient(ellipse at 50% 55%, #d9b89a 0%, #e8d3c2 35%, #f2ece6 60%, #ffffff 85%);
  }
  .event-title {
    position: absolute; right: 30px; top: 585px; text-align: right;
    font-family: "Anton", Impact, sans-serif; color: #fff;
    text-shadow: -1px -1px 0 #888, 1px -1px 0 #888, -1px 1px 0 #888, 5px 5px 3px var(--shadow);
    line-height: 1.08;
  }
  .event-title .name { display: block; font-size: 74px; }
  .event-title .place { display: block; font-size: 60px; padding-right: 6px; }
  .info-row {
    position: absolute; left: 0; width: 818px; display: flex;
    font-family: "Anton", Impact, sans-serif; color: #fff;
    text-shadow: 3px 3px 3px var(--shadow);
  }
  .info-row .label { width: 229px; border-right: 3px solid var(--rule); padding: 22px 0 0 42px; font-size: 44px; }
  .info-row .value { flex: 1; padding: 22px 0 0 40px; }
  .when { top: 750px; height: 156px; background: var(--purple); border-bottom: 3px solid var(--rule); }
  .when .value { font-size: 46px; line-height: 60px; }
  .where { top: 906px; height: 136px; background: var(--blue); }
  .where .value { font-size: 31px; line-height: 40px; padding-top: 14px; }
  .where .label { padding-top: 16px; }
  .site-band {
    position: absolute; left: 0; top: 1042px; width: 818px; height: 80px;
    background: var(--teal); border-top: 3px solid var(--rule);
    font-family: "Anton", Impact, sans-serif; color: #fff; font-size: 50px;
    text-align: center; line-height: 76px;
    text-shadow: 4px 4px 3px var(--shadow);
  }
  .organizer {
    position: absolute; left: 0; top: 1128px; width: 818px; text-align: center;
    font-family: "Roboto", Arial, sans-serif; font-size: 10px; color: var(--ink);
  }
</style>
</head>
<body>
  <article class="flyer">
    <header class="headline-band">
      <span class="l1">Damit Kinder ihre aktuellen und</span>
      <span class="l2">zukünftigen Herausforderungen</span>
      <span class="l3">spielend meistern!</span>
    </header>
    <div class="brand">
      <div class="brand-dot"></div>
      <div class="brand-name">Funken und Fragen</div>
      <div class="brand-url">www.funkenundfragen.ch</div>
    </div>
    <div class="photo" role="img" aria-label="Foto: zwei Kinder basteln am Tisch mit Leim und buntem Papier"></div>
    <h1 class="event-title">
      <span class="name">Funken und Fragen</span>
      <span class="place">Messe Zürich</span>
    </h1>
    <section class="info-row when">
      <div class="label">Wann?</div>
      <div class="value">So. 9. November 2012<br>11-18 Uhr</div>
    </section>
    <section class="info-row where">
      <div class="label">Wo?</div>
      <div class="value">Seeforumhalle - Lindensaal<br>Wendelgasse 7<br>8047 Zürich</div>
    </section>
    <div class="site-band">www.funkenundfragen.ch</div>
    <footer class="organizer"><strong>Veranstalter:</strong> FunkenundFragen GmbH, Am Talbach 12, 8815 Horgenberg</footer>
  </article>
</body>
</html>
```